Billboard Design for Modern Dispensary

Hello!
We need a eye-catching 12' x 24' billboard designed for a very successful, modern cannabis dispensary on the Oregon coast, United States. Because of rules, we cannot have any marijuana leafs or other cannabis related images (flower, joints, smoke, etc). We can use the words "Shop" or "Dispensary" - we cannot use the words "cannabis", "marijuana".

Some ideas we had are 3 words stacked on left or center of billboard - maybe across bottom we have horizontal logo and the following words - “South of bridge in Seal Cove”
Another idea is to have a small bubble in bottom/top corner with image of our dog (face only) - with some words around it - like "BONUS Shop Dog" or "Cute Shop Dog" or "Best Shop Dog" or "Friendly Staff"

here's some 3 word examples:
ENJOY
YOUR
TRIP

or

FEEL
GOOD
JUST
AHEAD

or

GOOD
VIBES
ONLY

or

GOOD
TIMES
CHILL
VIBES

I have attached our logo. I have also included a stacked logo version (vertical, not horizontal). the formats are .EPS and .PDF - the logos were created in Affinity Design 2.x.

Our website is coralnook.net if you want to see more images, etc about our dispensary.

Artwork Requirements:
The billboard is 12' tall x 25' wide
The artwork needs to be 1”=1’ @ 300dpi
Please add 6” of bleed all around so your total artwork is 13”x26”
Final deliverable should be .Ai file.

Font styles to use
Sans Serif

Colors
0054AA
0677BA
7BADD7
CADEEF
E8F1F8

Requirements
Nice to have
• See the project description - we included some ideas to consider.
Should not have
• No cannabis images, like flower, cannabis leaves, paraphenlia, cartridges, joints, etc.

```html
<!DOCTYPE html>
<html lang="en">
<head>
<meta charset="utf-8">
<title>Coral Nook Billboard</title>
<link rel="stylesheet" href="https://fonts.googleapis.com/css2?family=Poppins:wght@400;600;700;800&display=swap">
<style>
  :root {
    --sky-blue: #3d9bd8;
    --ink: #0a0a0a;
    --paper: #ffffff;
    --stage: #111111;
    --fur: #c9a06a;
  }
  html, body {
    margin: 0;
    width: 1200px;
    height: 907px;
    overflow: hidden;
    background: var(--stage);
  }
  .billboard {
    position: absolute;
    left: 0;
    top: 164px;
    width: 1200px;
    height: 579px;
    display: block;
  }
  .panel-blue { fill: var(--sky-blue); }
  .panel-ink { fill: var(--ink); }
  .panel-paper { fill: var(--paper); }
  .divider-line { fill: none; stroke: var(--ink); stroke-width: 12; }
  .brand-ring { fill: none; stroke: var(--sky-blue); stroke-width: 16; }
  .brand-name {
    font-family: "Poppins", sans-serif;
    font-weight: 400;
    font-size: 72px;
    fill: var(--sky-blue);
  }
  .location {
    font-family: "Poppins", sans-serif;
    font-weight: 600;
    font-size: 46px;
    fill: var(--ink);
  }
  .headline {
    font-family: "Poppins", sans-serif;
    font-weight: 800;
    font-size: 160px;
    fill: var(--paper);
    letter-spacing: -2px;
  }
  .badge-outer { fill: var(--paper); }
  .badge-ring { fill: var(--sky-blue); }
  .badge-photo { fill: var(--fur); }
  .badge-text {
    font-family: "Poppins", sans-serif;
    font-weight: 700;
    font-size: 14px;
    letter-spacing: 2px;
    fill: var(--paper);
  }
</style>
</head>
<body>
<svg class="billboard" viewBox="0 0 1483 716" xmlns="http://www.w3.org/2000/svg">
  <defs>
    <path id="badge-top-arc" d="M586,601 A52,52 0 0 1 690,601"/>
    <path id="badge-bottom-arc" d="M574,601 A64,64 0 0 0 702,601"/>
  </defs>

  <!-- Right field -->
  <rect class="panel-ink" x="0" y="85" width="1483" height="547"/>
  <rect class="panel-blue" x="0" y="0" width="1483" height="85"/>
  <rect class="panel-blue" x="0" y="632" width="1483" height="84"/>

  <!-- Curved divider -->
  <path class="panel-blue" d="M0,0 H573 A471,471 0 0 1 573,716 H0 Z"/>
  <path class="panel-paper" d="M0,0 H544 A453,453 0 0 1 544,716 H0 Z"/>
  <path class="divider-line" d="M467,0 A410,410 0 0 1 467,716"/>

  <!-- Brand -->
  <circle class="brand-ring" cx="316" cy="228" r="80"/>
  <text class="brand-name" x="316" y="383" text-anchor="middle">CORAL NOOK</text>

  <text class="location" text-anchor="middle">
    <tspan x="321" y="523">SOUTH OF BRIDGE IN</tspan>
    <tspan x="321" y="575">SEAL COVE</tspan>
  </text>

  <!-- Headline -->
  <text class="headline">
    <tspan x="783" y="244">BEST</tspan>
    <tspan x="783" y="413">SHOP</tspan>
    <tspan x="783" y="582">PERIOD</tspan>
  </text>

  <!-- Shop dog badge -->
  <g class="shop-dog-badge">
    <circle class="badge-outer" cx="638" cy="601" r="80"/>
    <circle class="badge-ring" cx="638" cy="601" r="69"/>
    <circle class="badge-photo" cx="638" cy="601" r="46" role="img" aria-label="Photo of the shop dog's face"/>
    <text class="badge-text" text-anchor="middle"><textPath href="#badge-top-arc" startOffset="50%">BONUS</textPath></text>
    <text class="badge-text" text-anchor="middle"><textPath href="#badge-bottom-arc" startOffset="50%">SHOP DOG</textPath></text>
  </g>
</svg>
</body>
</html>
```